Elm Ridge Baptist Church sign

We want a colourful, attractive sign that includes connection to being a Christian Church living in the foothills of the Canadian Rocky Mountains. As far as printed words, we need it to say “ Elm Ridge Baptist Church”. We are planning on a sign that is 6’ x 4’. Our church slogan is:
“ Live like Jesus, Love like Jesus”. This slogan could be included on the sign if space allows. To all designers; in talking with the communications team at our church, we want to eliminate the church’s slogan “ live like Jesus, live like Jesus “, from being on the sign.

```html
<!DOCTYPE html>
<html lang="en">
<head>
<meta charset="UTF-8">
<title>Elm Ridge Baptist Church — Sign</title>
<link rel="stylesheet" href="https://fonts.googleapis.com/css2?family=Montserrat:wght@800&display=swap">
<style>
  :root {
    --backdrop-light: #ead9cb;
    --backdrop-mid: #dcc6b5;
    --backdrop-deep: #cfb6a3;
    --name-red: #7a2e31;
    --ink-dark: #323232;
  }
  html, body {
    margin: 0;
    padding: 0;
    overflow: hidden;
    background: #ffffff;
  }
  .sign {
    position: relative;
    width: 1200px;
    height: 846px;
    overflow: hidden;
  }
  .sign__backdrop {
    position: absolute;
    inset: 0;
    background:
      radial-gradient(ellipse at 50% 45%, var(--backdrop-light) 0%, var(--backdrop-mid) 70%, var(--backdrop-deep) 100%);
  }
  .sign__title {
    margin: 0;
    font-size: inherit;
  }
  .sign__name {
    position: absolute;
    right: 206px;
    font-family: "Montserrat", sans-serif;
    font-weight: 800;
    font-size: 214px;
    line-height: 1;
    letter-spacing: -4px;
    color: var(--name-red);
    opacity: 0.92;
    text-align: right;
    white-space: nowrap;
  }
  .sign__name--first { top: 141px; }
  .sign__name--second { top: 321px; }
  .sign__subtitle {
    position: absolute;
    right: 253px;
    top: 519px;
    margin: 0;
    font-family: "Montserrat", sans-serif;
    font-weight: 800;
    font-size: 70px;
    line-height: 1;
    letter-spacing: -2.5px;
    color: var(--ink-dark);
    text-align: right;
    white-space: nowrap;
  }
</style>
</head>
<body>
  <main class="sign">
    <div class="sign__backdrop" role="img" aria-label="Softly faded photograph of a Gothic cathedral interior with tall pillars and vaulted arches"></div>
    <h1 class="sign__title">
      <span class="sign__name sign__name--first">ELM</span>
      <span class="sign__name sign__name--second">RIDGE</span>
    </h1>
    <p class="sign__subtitle">BAPTIST CHURCH</p>
  </main>
</body>
</html>
```